Modern Dry eye Poster for eye center, Optometrist office

We need a banner to connect to patient about dry eye and treatment. Ask if patient has dry eyes and we offer treatment .
What is dry eye?
Are you suffering for dry, gritty, painful eyes, blurred vision, redness..

Now there is a quick, comfortable and affordable procedure offering relief tofdry eye.

Schedule your dry eye treatment today.

Target Market(s)

Dry eye patient

Font styles to use
Sans Serif

Colors
00a990
ffffff
0492cd
fbf289
85cae6

Requirements
Must have
• Modern design, dry eye patient
Nice to have
• real life model of nice eyes
Should not have
• No cartoon,

```html
<!DOCTYPE html>
<html lang="en">
<head>
<meta charset="utf-8">
<title>What is dry eye?</title>
<link rel="stylesheet" href="https://fonts.googleapis.com/css2?family=Source+Sans+3:wght@300;400;600;700&display=swap">
<style>
  :root {
    --paper: #ffffff;
    --slate: #7a8a89;
    --sun: #f6d41c;
    --ink-teal: #52706e;
    --brand-grey: #6f7474;
    --skin-light: #efc3b3;
    --skin-rose: #d99a8a;
    --skin-mauve: #b27468;
    --skin-deep: #8f5a50;
    --shade: #6f8d96;
    --shade-deep: #56707a;
  }
  * { margin: 0; padding: 0; box-sizing: border-box; }
  html, body {
    width: 1200px; height: 2517px; overflow: hidden;
    background: var(--paper);
    font-family: "Source Sans 3", "Myriad Pro", Arial, sans-serif;
  }
  .poster { position: relative; width: 1200px; height: 2517px; background: var(--paper); }

  .title-block {
    position: absolute; left: 117px; top: 0; width: 774px; height: 450px;
    background: var(--slate); color: var(--paper);
  }
  .title-main {
    position: absolute; left: 66px; top: 112px;
    font-size: 186px; font-weight: 700; line-height: 1; letter-spacing: -6px;
  }
  .title-sub {
    position: absolute; left: 275px; top: 262px;
    font-size: 138px; font-weight: 300; line-height: 1; letter-spacing: -3px;
  }

  .question-band {
    position: absolute; left: 0; top: 450px; width: 1200px; height: 176px;
    background: var(--sun); color: var(--paper);
    display: flex; align-items: center; justify-content: center;
    font-size: 84px; font-weight: 600; letter-spacing: -0.5px;
  }

  .model-photo {
    position: absolute; left: 0; top: 626px; width: 1200px; height: 1349px;
    background:
      linear-gradient(180deg, rgba(120,70,62,0.35) 0%, rgba(120,70,62,0) 22%, rgba(120,70,62,0) 70%, rgba(110,66,60,0.25) 100%),
      linear-gradient(90deg,
        var(--skin-light) 0%,
        var(--skin-rose) 30%,
        var(--skin-mauve) 55%,
        var(--skin-deep) 78%,
        var(--shade) 90%,
        var(--shade-deep) 100%);
  }

  .symptom-list {
    position: absolute; left: 527px; top: 980px; width: 600px;
    list-style: none; text-align: center; color: var(--paper);
    font-size: 102px; font-weight: 300; line-height: 120px; letter-spacing: -1px;
  }

  .call-to-action {
    position: absolute; left: 134px; top: 2100px;
    color: var(--ink-teal); font-size: 70px; font-weight: 400; line-height: 80px;
  }

  .brand { position: absolute; left: 815px; top: 2030px; width: 300px; text-align: center; }
  .brand-square {
    width: 220px; height: 220px; margin: 0 auto 96px;
    background: var(--sun);
  }
  .brand-name {
    color: var(--brand-grey); font-size: 42px; font-weight: 300;
    line-height: 46px; letter-spacing: 4px; text-transform: uppercase;
  }
</style>
</head>
<body>
<main class="poster">
  <header class="title-block">
    <h1 class="title-main">What is</h1>
    <p class="title-sub">dry eye?</p>
  </header>

  <div class="question-band">Are you suffering for</div>

  <div class="model-photo" role="img" aria-label="Close-up photograph of a woman's blue eye with a fingertip gently pulling down the lower eyelid"></div>

  <ul class="symptom-list">
    <li>dry</li>
    <li>gritty</li>
    <li>redness</li>
    <li>painful eyes</li>
    <li>blurred vision</li>
  </ul>

  <p class="call-to-action">Schedule your dry eye<br>treatment today.</p>

  <div class="brand">
    <div class="brand-square"></div>
    <p class="brand-name">Brightview<br>Optometry</p>
  </div>
</main>
</body>
</html>
```